Graphics Design of Physics Book

Hi
Size : 8" x 11.25"
We are education book Publication Company and would like to have book cover for "Physics" it has 4 volumes. All 4 having the same color scheme and design except the volume no.
Blue is my personal favorite but u can use any color. Want to have a band at the bottom of the cover to place our Logo “VORLIN Education” a PDF of the same is attached, or you can place logo anywhere according to ur design.
I need “Physics” as title of the book to be visible prominently.
And volume and volume no. should also be Visible and eye catching I prefer a Graphic to enhance the Volume No.
A background pattern can also be a option (it should be vector form so that color can be change later)
Please do not offer any cut and paste design I need very professional presentation.
Volume and Number can be in metallic 3D (CMYK) effect.
only Professional presentation will get feedback.
I have provided a sample artwork for reference do not follow it but can be a reference what I needed !

Target Market(s)

Students Class 9th to 12th

Industry/Entity Type

Education

Font styles to use
Serif

Colors
3176b5
0555a3
85abd2
cadf82
abd036
9bcb3c

Requirements
Must have
• Eye catching.
• “Physics” as title of the book to be visible prominently.
• volume and volume no. should also be Visible and eye catching
• I prefer a Graphic to enhance the Volume No.
• Icons for
• 1. Questions and answers
• 2. Theory Notes
• 3. Tips & Tricks
• 4. Previous Year's Reference Questions
• 5. Covers Complete Syllabus
Nice to have
• decent seamless background or metallic 3d effect (not to be print in special Ink) design should only be in CMYK.
Should not have
• Physics related Pictures or Icons (Specially E=mc2) or any scientist photograph or I Need pure graphic design

```html
<!DOCTYPE html>
<html lang="en">
<head>
<meta charset="utf-8">
<title>Physics Volume 1 — Book Cover</title>
<link href="https://fonts.googleapis.com/css2?family=Archivo+Black&family=PT+Sans:wght@400;700&display=swap" rel="stylesheet">
<style>
  :root {
    --cover-blue: #2f5ea8;
    --cover-blue-light: #3d73ba;
    --cover-blue-deep: #2a559c;
    --rule-blue: #24498a;
    --tile: #8aaad6;
    --tile-edge: #a9c2e4;
    --ink: #1d1f24;
    --white: #ffffff;
    --label: #f2f5fb;
    --band-light: #f4f4f4;
    --band-mid: #b9b9b9;
    --band-dark: #8c8c8c;
  }
  * { margin: 0; padding: 0; box-sizing: border-box; }
  html, body { width: 853px; height: 1200px; overflow: hidden; background: var(--cover-blue); }
  .cover {
    position: relative;
    width: 853px; height: 1200px;
    background: radial-gradient(ellipse 60% 45% at 50% 48%, var(--cover-blue-light), var(--cover-blue) 70%, var(--cover-blue-deep));
    font-family: "PT Sans", sans-serif;
  }
  .rule {
    position: absolute; left: 24px; width: 802px; height: 2px;
    background: var(--rule-blue);
  }
  .rule--top { top: 101px; }
  .rule--bottom { top: 372px; }
  .title { position: absolute; left: 40px; top: 120px; width: 775px; height: 230px; }
  .title text { font-family: "Archivo Black", sans-serif; }
  .volume {
    position: absolute; right: 36px; top: 398px;
    font-family: "PT Sans", sans-serif; font-weight: 700;
    font-size: 74px; color: var(--white); letter-spacing: -1px;
    line-height: 1;
  }
  .feature {
    position: absolute; width: 180px; margin-left: -90px;
    text-align: center; color: var(--label);
    font-size: 21px; line-height: 23px;
  }
  .feature__tile {
    display: block; width: 116px; height: 116px; margin: 0 auto 18px;
    border-radius: 20px; background: var(--tile);
    border: 2px solid var(--tile-edge);
    box-shadow: 0 4px 8px rgba(10, 30, 70, 0.35);
  }
  .feature__tile svg { width: 100%; height: 100%; display: block; }
  .band {
    position: absolute; left: 0; top: 1086px; width: 853px; height: 66px;
    background: linear-gradient(100deg, var(--band-mid) 0%, var(--band-light) 18%, var(--band-dark) 40%, var(--band-light) 60%, var(--band-mid) 80%, var(--band-light) 100%);
    display: flex; align-items: center; justify-content: center;
  }
  .publisher {
    font-family: "PT Sans", sans-serif; font-weight: 700;
    font-size: 26px; letter-spacing: 3px; color: var(--ink);
  }
</style>
</head>
<body>
<main class="cover">
  <div class="rule rule--top"></div>

  <svg class="title" viewBox="0 0 775 230" aria-label="Physics">
    <defs>
      <linearGradient id="chrome" x1="0" y1="0" x2="1" y2="0">
        <stop offset="0" stop-color="#f7f7f7"/>
        <stop offset="0.08" stop-color="#9a9a9a"/>
        <stop offset="0.16" stop-color="#ffffff"/>
        <stop offset="0.28" stop-color="#a3a3a3"/>
        <stop offset="0.38" stop-color="#f0f0f0"/>
        <stop offset="0.5" stop-color="#9c9c9c"/>
        <stop offset="0.62" stop-color="#ffffff"/>
        <stop offset="0.74" stop-color="#a0a0a0"/>
        <stop offset="0.86" stop-color="#f5f5f5"/>
        <stop offset="1" stop-color="#a8a8a8"/>
      </linearGradient>
    </defs>
    <text x="2" y="204" font-size="262" textLength="770" lengthAdjust="spacingAndGlyphs"
          fill="url(#chrome)" stroke="#ffffff" stroke-width="2">Physics</text>
  </svg>

  <div class="rule rule--bottom"></div>

  <div class="volume">Volume1</div>

  <div class="feature" style="left:158px; top:592px;">
    <span class="feature__tile">
      <svg viewBox="0 0 64 64" fill="none" stroke="#1d1f24" stroke-width="3.2" stroke-linejoin="round">
        <path d="M34 26 a16 13 0 1 1 17 17 l3 7 -9 -5"/>
        <path d="M8 26 a16 13 0 1 1 9 12 l-6 6 1 -9 a13 13 0 0 1 -4 -9z" fill="#8aaad6"/>
        <text x="11" y="31" font-family="Archivo Black, sans-serif" font-size="13" fill="#1d1f24" stroke="none">Q</text>
        <text x="22" y="32" font-family="PT Sans, sans-serif" font-size="8" fill="#1d1f24" stroke="none">&amp;</text>
        <text x="28" y="30" font-family="Archivo Black, sans-serif" font-size="13" fill="#1d1f24" stroke="none">A</text>
      </svg>
    </span>
    Questions<br>&amp; Answers
  </div>

  <div class="feature" style="left:426px; top:592px;">
    <span class="feature__tile">
      <svg viewBox="0 0 64 64" fill="none" stroke="#1d1f24" stroke-width="3" stroke-linejoin="round" stroke-linecap="round">
        <path d="M24 12 h-7 v40 h20"/>
        <path d="M40 12 h7 v22"/>
        <rect x="24" y="9" width="16" height="7" rx="2"/>
        <path d="M22 25 l2 2 4 -4 M32 25 h10 M22 34 l2 2 4 -4 M32 34 h8 M22 43 l2 2 4 -4 M32 43 h3"/>
        <circle cx="47" cy="47" r="8" fill="#1d1f24"/>
        <path d="M43 47 l3 3 5 -6" stroke="#8aaad6" stroke-width="2.4"/>
      </svg>
    </span>
    Complete<br>Syllabus
  </div>

  <div class="feature" style="left:694px; top:592px;">
    <span class="feature__tile">
      <svg viewBox="0 0 64 64" fill="none" stroke="#1d1f24" stroke-width="3.2" stroke-linecap="round">
        <path d="M15 40 A19 19 0 1 0 14 24"/>
        <path d="M9 40 l6 0 0 -6" stroke-linejoin="round"/>
        <path d="M32 32 l6 -10 M32 32 l-9 4"/>
        <circle cx="32" cy="32" r="2" fill="#1d1f24"/>
      </svg>
    </span>
    Reference<br>Questions
  </div>

  <div class="feature" style="left:286px; top:838px;">
    <span class="feature__tile">
      <svg viewBox="0 0 64 64" fill="none" stroke="#1d1f24" stroke-width="3.4" stroke-linejoin="round" stroke-linecap="round">
        <path d="M36 15 h-22 v36 h36 v-22"/>
        <path d="M46 10 l7 7 -20 20 -9 2 2 -9z"/>
      </svg>
    </span>
    Theory Notes
  </div>

  <div class="feature" style="left:572px; top:838px;">
    <span class="feature__tile">
      <svg viewBox="0 0 64 64" fill="none" stroke="#1d1f24" stroke-width="3" stroke-linecap="round" stroke-linejoin="round">
        <path d="M25 42 c0 -6 -6 -8 -6 -15 a13 13 0 0 1 26 0 c0 7 -6 9 -6 15z"/>
        <path d="M26 46 h12 M27 50 h10 M29 54 h6"/>
        <path d="M32 6 v5 M18 11 l3 4 M46 11 l-3 4 M10 22 l5 2 M54 22 l-5 2 M9 33 h5 M50 33 h5"/>
      </svg>
    </span>
    Tips &amp; Tricks
  </div>

  <footer class="band">
    <span class="publisher">VORLIN EDUCATION</span>
  </footer>
</main>
</body>
</html>
```